Flyer-Design für Fitness-Studio für Frauen & Männer über 50
Von Anfang an den Nagel auf den Kopf getroffen! danke.
Zielgruppe
Athletic * Fitness * Nutrition
Wir sind Gym mit funktionellen workouts. die zielgruppe für den flyer sind frauen und männer im alter über 50.
Aufgabenstellung
Soll Menschen über 50 ansprechen.

```html
<!DOCTYPE html>
<html lang="de">
<head>
<meta charset="utf-8">
<title>FORTIS – Vitality 50+ Flyer</title>
<link href="https://fonts.googleapis.com/css2?family=Bebas+Neue&family=Poppins:wght@400;600&display=swap" rel="stylesheet">
<style>
  :root {
    --red: #b42f31;
    --black: #1e1e1e;
    --grey: #bfbfbf;
    --ring: #c4c4c4;
    --text: #222222;
    --white: #ffffff;
    --page: #ffffff;
  }
  html, body { margin: 0; padding: 0; overflow: hidden; }
  body { width: 1200px; height: 1200px; background: var(--page); position: relative; font-family: "Poppins", sans-serif; color: var(--text); }
  .panel { position: absolute; top: 78px; width: 452px; height: 958px; overflow: hidden; background: var(--white); box-shadow: 3px 3px 6px rgba(0,0,0,.25); }
  .panel--front { left: 124px; }
  .panel--back { left: 652px; }
  .panel__shapes { position: absolute; inset: 0; width: 100%; height: 100%; }
  .abs { position: absolute; margin: 0; white-space: nowrap; }

  .brand-name { left: 24px; top: 58px; font-family: "Bebas Neue", sans-serif; font-weight: 400; font-size: 80px; line-height: 1; color: var(--black); letter-spacing: 1px; }

  .offer-title { left: 23px; top: 528px; font-family: "Bebas Neue", sans-serif; font-weight: 400; color: var(--white); }
  .offer-title .big { display: block; font-size: 42px; line-height: 48px; }
  .offer-title .line { display: block; font-size: 28px; line-height: 34px; }

  .offer-price { left: 280px; top: 518px; font-family: "Bebas Neue", sans-serif; font-size: 22px; line-height: 27px; color: var(--black); }

  .studio { left: 23px; top: 746px; font-weight: 600; font-size: 15px; line-height: 19.5px; color: var(--black); }
  .coach { left: 23px; top: 804px; font-size: 15px; line-height: 19.5px; color: var(--black); }
  .contact { left: 23px; top: 881px; font-size: 15px; line-height: 19.5px; color: var(--black); }
  .contact strong { font-weight: 600; }

  .benefits-title { left: 23px; top: 281px; font-weight: 600; font-size: 15px; line-height: 20px; color: var(--red); }
  .benefits { left: 23px; top: 321px; font-size: 15px; line-height: 19.4px; list-style: none; padding: 0; }
  .benefits li::before { content: "• "; }
  .copy { left: 23px; font-size: 15px; line-height: 19.4px; }
  .copy strong { font-weight: 600; }
  .copy--1 { top: 456px; }
  .copy--2 { top: 572px; }
  .copy--3 { top: 707px; }
  .web { left: 281px; top: 920px; font-weight: 600; font-size: 15px; line-height: 20px; color: var(--black); }
</style>
</head>
<body>

<section class="panel panel--front">
  <svg class="panel__shapes" viewBox="0 0 723 1532" preserveAspectRatio="none">
    <defs>
      <linearGradient id="photoSeniors" x1="0" y1="0" x2="1" y2="1">
        <stop offset="0" stop-color="#e3e8ec"/>
        <stop offset=".55" stop-color="#b9c6cc"/>
        <stop offset="1" stop-color="#3f6f80"/>
      </linearGradient>
      <linearGradient id="photoCoach" x1="0" y1="0" x2="0" y2="1">
        <stop offset="0" stop-color="#8a8a8a"/>
        <stop offset="1" stop-color="#2b3038"/>
      </linearGradient>
    </defs>
    <rect width="723" height="1532" fill="var(--grey)"/>
    <polygon points="0,505 723,105 723,1532 0,1532" fill="var(--white)"/>
    <polygon points="0,505 723,68 723,110 0,510" fill="var(--red)"/>
    <polygon role="img" aria-label="Foto: zwei ältere Menschen bei Dehnübungen im Fitnessstudio" points="0,512 723,112 723,757 395,815 0,830" fill="url(#photoSeniors)"/>
    <polygon points="0,1000 580,1210 723,1290 723,1532 0,1532" fill="var(--red)"/>
    <polygon points="580,1192 723,1262 723,1288 580,1210" fill="var(--grey)"/>
    <circle cx="190" cy="930" r="212" fill="var(--black)"/>
    <circle cx="430" cy="1173" r="153" fill="var(--ring)"/>
    <circle role="img" aria-label="Foto: Trainer mit Kappe im Studio" cx="430" cy="1173" r="147" fill="url(#photoCoach)"/>
  </svg>

  <p class="abs brand-name">FORTIS</p>

  <h1 class="abs offer-title">
    <span class="big">AKTION</span>
    <span class="line">GESUNDHEITSFÖRDERUNG</span>
    <span class="line">VITALITY 50+</span>
  </h1>

  <p class="abs offer-price">PERSONAL TRAINING /<br>COACHING<br>FÜR CHF 50.00<br>PRO STUNDE</p>

  <p class="abs studio">FORTIS®<br>Seeburg</p>
  <p class="abs coach">Lukas Brandner<br>Dipl. Athletic Coach<br>KMX-Diplom Caliper</p>
  <p class="abs contact">Weitere Informationen:<br>041 555 12 34<br><strong>www.fortis-beispiel.ch</strong></p>
</section>

<section class="panel panel--back">
  <svg class="panel__shapes" viewBox="0 0 723 1532" preserveAspectRatio="none">
    <defs>
      <linearGradient id="photoGym" x1="0" y1="0" x2="1" y2="1">
        <stop offset="0" stop-color="#c9b8a6"/>
        <stop offset=".6" stop-color="#8c7b6c"/>
        <stop offset="1" stop-color="#4c4a4e"/>
      </linearGradient>
      <linearGradient id="photoPushup" x1="0" y1="0" x2="0" y2="1">
        <stop offset="0" stop-color="#d9dde0"/>
        <stop offset="1" stop-color="#6e747a"/>
      </linearGradient>
      <linearGradient id="photoTowel" x1="0" y1="0" x2="0" y2="1">
        <stop offset="0" stop-color="#9aa0a6"/>
        <stop offset="1" stop-color="#4f6a8d"/>
      </linearGradient>
      <linearGradient id="photoDumbbell" x1="0" y1="0" x2="1" y2="1">
        <stop offset="0" stop-color="#a8a6a8"/>
        <stop offset="1" stop-color="#4a4a4c"/>
      </linearGradient>
    </defs>
    <rect width="723" height="1532" fill="var(--white)"/>
    <polygon role="img" aria-label="Foto: lächelnde ältere Frau beim Training im Fitnessstudio" points="0,0 723,0 723,478 0,72" fill="url(#photoGym)"/>
    <polygon points="0,72 723,478 723,505 0,102" fill="var(--red)"/>
    <polygon points="300,1400 723,1148 723,1532 300,1532" fill="var(--red)"/>
    <polygon points="300,1396 723,1144 723,1152 300,1406" fill="var(--black)"/>
    <circle cx="197" cy="240" r="143" fill="var(--ring)"/>
    <circle role="img" aria-label="Foto: zwei ältere Menschen bei Liegestützen" cx="197" cy="240" r="137" fill="url(#photoPushup)"/>
    <circle cx="524" cy="425" r="138" fill="var(--ring)"/>
    <circle role="img" aria-label="Foto: lächelnder älterer Mann mit Handtuch" cx="524" cy="425" r="132" fill="url(#photoTowel)"/>
    <circle cx="177" cy="1418" r="143" fill="var(--ring)"/>
    <circle role="img" aria-label="Foto: Frau beim Training mit Kurzhantel" cx="177" cy="1418" r="137" fill="url(#photoDumbbell)"/>
  </svg>

  <h2 class="abs benefits-title">Ihr Nutzen auf einen Blick</h2>
  <ul class="abs benefits">
    <li>Standortbestimmung</li>
    <li>Zielvereinbarung</li>
    <li>Trainings- und Ernährungsempfehlungen</li>
    <li>Caliper Hautfaltenmessung</li>
    <li>Fitnesstests</li>
    <li>Individuelle Unterstützung und Motivation</li>
  </ul>

  <p class="abs copy copy--1">Sind Sie 50+ und möchten Ihr Leben vital und selbst-<br>bewusst gestalten? Sie wollen in Zukunft mehr<br>Wert auf Ihre Gesundheit und Fitness legen oder<br>Ihren Bodymass-Index verbessern? Dann sind Sie<br>bei <strong>FORTIS®</strong> genau richtig!</p>
  <p class="abs copy copy--2">Ihre Kinder sind ausgeflogen? Sie suchen neben<br>Ihrer Arbeit – sei es zuhause oder im Büro – einen<br>sportlichen Ausgleich? <strong>FORTIS®</strong> unterstützt<br>Sie dabei. Gemeinsam definieren wir, welche Bewe-<br>gungsformen zu Ihnen und Ihrem individuellen Alltag<br>passen, damit Sie Ihre persönlichen Ziele erreichen.</p>
  <p class="abs copy copy--3">Das Personal Training / Coaching findet bei<br><strong>FORTIS®</strong> oder bequem bei Ihnen zuhause<br>statt. Wir freuen uns auf Sie!</p>

  <p class="abs web">www.fortis-beispiel.ch</p>
</section>

</body>
</html>
```